Webpages for Sammalkivi Software Consulting

Needed: Webpage design.
Details:
One page site with good looking fonts and simple modern design. Logo would also be nice.
Page is for Software consulting company called: "Sammalkivi Software Consulting". Sammalkivi is my surname.
Pages should tell viewer that the company is reliable and its employees are hard-core professionals.
Company currently has one employee, that's me. So what I do is what this company does. I am software consultant. Basicly that means that I do Java/JavaEE/Web programming as subcontractor.
Here is more detail information about me.
SPECIALTIES
- Enterprise J2EE Application Programming and Architectures,
- Web development and
- Agile development.
I have over a decade of experience on designing and creating Java based web-services and applications to multiple interfaces. I also have plenty of experience about software architectures, design patterns and integration into third party systems. I’ve got good knowledge about agile software development and testing processes and I am experienced ScrumMaster and software project leader.
Target Market(s)
IT Businesses, Coding companies... Anyone who is buying coding as service.
Industry/Entity Type
Software

```html
<!DOCTYPE html>
<html lang="en">
<head>
<meta charset="utf-8">
<title>Sammalkivi Software Consultancy</title>
<link rel="stylesheet" href="https://fonts.googleapis.com/css2?family=Kreon:wght@400;700&family=Oswald:wght@400;500&family=Arimo:wght@400;700&display=swap">
<style>
:root{
  --lime:#b4cc10;
  --blue:#1570e8;
  --cyan:#2fb7e6;
  --ink:#2a2a2a;
  --grey:#8a8a8a;
  --grey-light:#a9a9a9;
  --page:#ececec;
  --navy:#1c2b39;
  --navy-line:#34485a;
  --link:#28b6e8;
  --red:#d01a1a;
}
*{box-sizing:border-box;margin:0;padding:0}
html,body{width:726px;height:1200px;overflow:hidden}
body{position:relative;background:var(--page);font-family:"Arimo",Arial,sans-serif;color:var(--ink)}
.abs{position:absolute}
.top-rule{left:0;top:0;width:726px;height:3px;background:var(--lime)}

/* header */
.brand{left:30px;top:40px;display:flex;align-items:center;gap:10px}
.brand-mark{width:40px;height:40px;background:var(--lime)}
.brand-name{font-family:"Kreon",Georgia,serif;font-weight:700;font-size:25px;line-height:1.05;color:#2a9fc2}
.brand-name span{display:block;font-size:17px}
.search-label{left:435px;top:76px;font-family:"Kreon",Georgia,serif;font-weight:700;font-size:14px;color:#333;letter-spacing:.5px}
.search-box{left:434px;top:99px;width:278px;height:20px;display:flex}
.search-field{flex:1;background:#fff;border:1px solid #d3d3d3;font-size:9px;color:#b5b5b5;padding:4px 6px}
.search-btn{width:25px;background:var(--lime);display:flex;align-items:center;justify-content:center}
.search-hint{left:437px;top:129px;font-size:8px;color:#444}
.search-hint b{font-weight:400;color:var(--link)}
.nav{left:18px;top:169px;width:698px;height:46px;border-top:1px solid #dcdcdc;display:flex;align-items:center;justify-content:space-between;padding:0 10px}
.nav a{font-family:"Kreon",Georgia,serif;font-size:13px;color:#222;text-decoration:none;letter-spacing:.3px}
.nav i{width:1px;height:14px;background:#333}
.header-base{left:0;top:216px;width:726px;height:3px;background:#fff}
.hero-band{left:0;top:219px;width:726px;height:280px;background:linear-gradient(#efebe0,#ebe8e0 85%,var(--page))}

/* hero */
.hero{left:18px;top:229px;width:698px;height:260px;background:#9aa8ad;padding:6px}
.hero-inner{position:relative;width:100%;height:100%;background:#000;overflow:hidden}
.hero-art{position:absolute;left:0;top:0;width:400px;height:100%;background:linear-gradient(90deg,#0e2c58,#3a5a7c 40%,#162640 75%,#000)}
.tag{position:absolute;right:0;font-family:"Kreon",Georgia,serif;font-weight:700;font-size:25px;color:#fff;padding:2px 10px 0 15px;height:37px}
.tag-dreams{top:13px;width:231px;background:var(--lime)}
.tag-solutions{top:60px;width:186px;background:var(--blue)}
.hero-copy{position:absolute;left:400px;top:104px;width:282px;font-family:"Kreon",Georgia,serif;font-size:11.5px;line-height:14px;color:#fff}

/* sidebar */
.side{left:26px;top:512px;width:195px;height:333px;background:#f1f0f0;border:1px solid #c9c9c9;border-radius:14px;box-shadow:0 3px 5px rgba(0,0,0,.25);overflow:hidden}
.side-item{height:55.5px;border-bottom:1px solid #dcdcdc;display:flex;align-items:center;padding-left:10px;gap:12px}
.side-item:last-child{border-bottom:0}
.side-icon{width:30px;height:32px;border-radius:6px;flex:none}
.side-title{font-family:"Arimo",Arial,sans-serif;font-weight:700;font-size:12px;color:#8d8d8d}
.side-sub{font-size:8.5px;color:#7a7a7a;margin-top:2px}

/* services */
.card{width:237px;height:210px}
.card-head{font-family:"Oswald",Arial,sans-serif;font-size:12.5px;color:#7d7d7d;letter-spacing:.3px;height:24px;border-bottom:1px solid #dadada;padding-left:1px}
.card-pic{margin-top:8px;width:237px;height:78px;border:1px solid #cfcfcf;padding:2px;background:#fff}
.card-pic div{width:100%;height:100%}
.pic-dark{background:linear-gradient(135deg,#050505,#2a2a2a 55%,#0b0b0b)}
.pic-office{background:linear-gradient(90deg,#a8acb4,#e4e5e8 40%,#8a93a8 70%,#cfd2d8)}
.card-title{font-family:"Kreon",Georgia,serif;font-size:13px;color:#222;margin-top:8px}
.card-text{font-size:9.3px;line-height:12px;color:#8c8c8c;margin-top:6px}
.card-more{font-size:7.5px;color:var(--red);margin-top:14px;padding-top:0}
.card-foot{height:1px;background:linear-gradient(90deg,#fff,#d6d6d6,#fff);margin-top:4px}

/* footer */
.footer{left:18px;top:974px;width:698px;height:226px;background:var(--navy);border-radius:16px 16px 0 0}
.foot-head{font-family:"Oswald",Arial,sans-serif;font-size:13px;color:#fff;letter-spacing:.2px}
.quick{left:41px;top:986px}
.quick ul{list-style:none;margin-top:11px}
.quick li{font-size:9px;color:var(--link);line-height:16.7px}
.quick li::before{content:"";display:inline-block;width:3px;height:3px;background:#fff;margin:0 7px 2px 3px}
.subscribe{left:244px;top:986px}
.sub-field{width:178px;height:17px;background:#fff;border-radius:6px;font-size:8px;color:#222;padding:4px 9px;margin-top:8px}
.sub-field:first-of-type{margin-top:10px}
.sub-copy{width:210px;margin-top:8px;font-size:9.2px;line-height:12px;color:var(--link)}
.sub-btn{margin-top:10px;width:125px;height:24px;border-radius:4px;background:linear-gradient(#7fd3f7,#2aa2dc);display:flex;align-items:center;padding-left:10px;gap:9px;font-family:"Oswald",Arial,sans-serif;font-weight:500;font-size:11.5px;color:#0d2c45}
.follow{left:525px;top:988px}
.social{display:flex;gap:16px;margin-top:12px}
.social span{width:40px;height:40px;border-radius:8px}
.contact-head{margin-top:16px}
.contact-row{display:flex;align-items:center;gap:12px;color:#fff;margin-top:10px}
.contact-row.phone{font-size:13.5px;letter-spacing:.5px}
.contact-row.mail{font-size:11.5px;margin-top:14px}
.foot-rule{left:18px;top:1167px;width:698px;height:1px;background:var(--navy-line)}
.legal{left:0;top:1178px;width:726px;text-align:center;font-size:7.5px;color:#d8dde2}
.legal i{font-style:normal;margin:0 6px}
</style>
</head>
<body>
<div class="abs top-rule"></div>

<header>
  <div class="abs brand">
    <div class="brand-mark"></div>
    <div class="brand-name">Sammalkivi<span>Software Consultancy</span></div>
  </div>
  <div class="abs search-label">SEARCH</div>
  <div class="abs search-box">
    <div class="search-field">search this site</div>
    <div class="search-btn">
      <svg width="13" height="13" viewBox="0 0 13 13"><circle cx="7.5" cy="5.5" r="3.8" fill="none" stroke="#fff" stroke-width="1.8"/><line x1="5" y1="8" x2="1.5" y2="11.5" stroke="#fff" stroke-width="2.2" stroke-linecap="round"/></svg>
    </div>
  </div>
  <div class="abs search-hint">Advanced search? <b>Click here</b></div>
  <nav class="abs nav">
    <a>HOME</a><i></i><a>ABOUT US</a><i></i><a>SERVICES</a><i></i><a>PROJECTS</a><i></i><a>BLOG</a><i></i><a>CONTACT US</a>
  </nav>
  <div class="abs header-base"></div>
</header>

<div class="abs hero-band"></div>
<section class="abs hero">
  <div class="hero-inner">
    <div class="hero-art" role="img" aria-label="Illustration of a humanoid robot working on a floating transparent screen"></div>
    <div class="tag tag-dreams">Your Dreams</div>
    <div class="tag tag-solutions">Our Solutions</div>
    <p class="hero-copy">Lorem ipsum dolor sit amet, consectetur adipiscing elit. Proin posuere ipsum sit amet urna bibendum iaculis. Etiam faucibus ultricies diam ac facilisis. Maecenas eleifend iaculis vulputate.</p>
  </div>
</section>

<aside class="abs side">
  <div class="side-item"><div class="side-icon" style="background:linear-gradient(#cfe3f2,#7fa9c9)" role="img" aria-label="Office building icon"></div><div><div class="side-title">about Sammalkivi</div><div class="side-sub">Our Story</div></div></div>
  <div class="side-item"><div class="side-icon" style="background:linear-gradient(#7cc23a 30%,#fff 30%)" role="img" aria-label="Calendar icon"></div><div><div class="side-title">our Specialities</div><div class="side-sub">Events on the current year</div></div></div>
  <div class="side-item"><div class="side-icon" style="background:linear-gradient(135deg,#3a8fd8,#d8352a)" role="img" aria-label="Globe and shopping cart icon"></div><div><div class="side-title">testimonials</div><div class="side-sub">online market and strategy</div></div></div>
  <div class="side-item"><div class="side-icon" style="background:linear-gradient(135deg,#f0b020,#9a4ab0)" role="img" aria-label="Group of people icon"></div><div><div class="side-title">our Clients</div><div class="side-sub">see our community forum</div></div></div>
  <div class="side-item"><div class="side-icon" style="background:linear-gradient(135deg,#e8d24a,#7aa83a)" role="img" aria-label="Pencil icon"></div><div><div class="side-title">latest Blog</div><div class="side-sub">Our List of clients</div></div></div>
  <div class="side-item"><div class="side-icon" style="background:linear-gradient(135deg,#f7c21c,#e88a10);border-radius:50%" role="img" aria-label="Question speech icon"></div><div><div class="side-title">Question? Call Us</div><div class="side-sub">Fill the form with your queries</div></div></div>
</aside>

<main>
  <article class="abs card" style="left:235px;top:513px">
    <h2 class="card-head">J2EE PROGRAMMING</h2>
    <div class="card-pic"><div class="pic-dark" role="img" aria-label="Photo of a laptop on a dark desk"></div></div>
    <h3 class="card-title">Lorem ipsum</h3>
    <p class="card-text">Lorem ipsum dolor sit amet, consectetur adipiscing elit. Proin posuere ipsum sit amet urna bibendum iaculis. Etiam faucibus ultricies diam ac facilisis. Maecenas eleifend iaculis vulputate.</p>
    <p class="card-more">» read more</p><div class="card-foot"></div>
  </article>
  <article class="abs card" style="left:473px;top:513px">
    <h2 class="card-head">J2EE ARCHITECTURES</h2>
    <div class="card-pic"><div class="pic-office" role="img" aria-label="Photo of two businessmen working at a table in a high-rise office"></div></div>
    <h3 class="card-title">Lorem ipsum</h3>
    <p class="card-text">Lorem ipsum dolor sit amet, consectetur adipiscing elit. Proin posuere ipsum sit amet urna bibendum iaculis. Etiam faucibus ultricies diam ac facilisis. Maecenas eleifend iaculis vulputate.</p>
    <p class="card-more">» read more</p><div class="card-foot"></div>
  </article>
  <article class="abs card" style="left:235px;top:740px">
    <h2 class="card-head">WEB DEVELOPMENT</h2>
    <div class="card-pic"><div class="pic-dark" role="img" aria-label="Photo of a laptop on a dark desk"></div></div>
    <h3 class="card-title">Lorem ipsum</h3>
    <p class="card-text">Lorem ipsum dolor sit amet, consectetur adipiscing elit. Proin posuere ipsum sit amet urna bibendum iaculis. Etiam faucibus ultricies diam ac facilisis. Maecenas eleifend iaculis vulputate.</p>
    <p class="card-more">» read more</p><div class="card-foot"></div>
  </article>
  <article class="abs card" style="left:473px;top:740px">
    <h2 class="card-head">AGILE PROGRAMMING</h2>
    <div class="card-pic"><div class="pic-office" role="img" aria-label="Photo of two businessmen working at a table in a high-rise office"></div></div>
    <h3 class="card-title">Lorem ipsum</h3>
    <p class="card-text">Lorem ipsum dolor sit amet, consectetur adipiscing elit. Proin posuere ipsum sit amet urna bibendum iaculis. Etiam faucibus ultricies diam ac facilisis. Maecenas eleifend iaculis vulputate.</p>
    <p class="card-more">» read more</p><div class="card-foot"></div>
  </article>
</main>

<footer>
  <div class="abs footer"></div>
  <div class="abs quick">
    <h4 class="foot-head">QUICK LINKS</h4>
    <ul><li>Home</li><li>Our Company</li><li>Our Capapbilities</li><li>Our People</li><li>Sitemap</li><li>Contact us</li></ul>
  </div>
  <div class="abs subscribe">
    <h4 class="foot-head">SUBSCRIBE NEWSLETTERS</h4>
    <div class="sub-field">Your name</div>
    <div class="sub-field">Your email id</div>
    <p class="sub-copy">Lorem ipsum dolor sit amet, consectetur adipiscing elit. Proin posuere ipsum sit amet urna bibendum iaculis. Etiam faucibus ultricies diam ac facilisis. Maecenas eleifend iaculis vulputate.</p>
    <div class="sub-btn">SUBSCRIBE NOW
      <svg width="16" height="16" viewBox="0 0 16 16"><circle cx="8" cy="8" r="7" fill="#fff" stroke="#1d8fc8" stroke-width="1"/><path d="M5 8h6M8.5 5.2L11.2 8 8.5 10.8" fill="none" stroke="#1d8fc8" stroke-width="1.6" stroke-linecap="round" stroke-linejoin="round"/></svg>
    </div>
  </div>
  <div class="abs follow">
    <h4 class="foot-head">FOLLOW US</h4>
    <div class="social">
      <span style="background:#3a6fb8" role="img" aria-label="Social network link"></span>
      <span style="background:#4cb8e8" role="img" aria-label="Social network link"></span>
      <span style="background:#e8742a" role="img" aria-label="Blog link"></span>
    </div>
    <h4 class="foot-head contact-head">CONTACT US</h4>
    <div class="contact-row phone">
      <svg width="18" height="22" viewBox="0 0 18 22"><path d="M4 2c-2 1-3 3-2 7s4 9 8 11c2 1 4 0 5-2l-3-3-2 1c-2-1-4-5-4-7l2-1-1-4z" fill="#d8262a"/></svg>
      555 0142 380
    </div>
    <div class="contact-row mail">
      <svg width="22" height="18" viewBox="0 0 22 18"><rect x="1" y="3" width="15" height="11" rx="1" fill="#7cc23a"/><path d="M16 6l5-3v12l-5-3z" fill="#2fb7e6"/></svg>
      info@sammalkivi.fi
    </div>
  </div>
  <div class="abs foot-rule"></div>
  <div class="abs legal">© 2011, All Rights Reserved, Privacy Policy<i>|</i>Terms &amp; Conditions<i>|</i>Sitemap</div>
</footer>
</body>
</html>
```